Sunrise Table Breakfast Flyer

We require a flyer to promote our weekly breakfast for young people.

HVYN Harlow Valley Youth Network is a not-for-profit community based organisation that supports at risk young people aged 12-25 years old.

The idea of the breakfast is to target young people who may be sleeping rough, who may not receive regular meals and/or who just want to feel connected - however we advertise it to all young people so those attending do not feel stigmatised. The aim is that with regular attendance, young people may seek assistance from organisational staff for issues and barriers they may be facing.

We want a design that's eye catching, inviting and makes breakfast the main feature.

Target Market(s)

young people aged 12-25

Industry/Entity Type

Community

Requirements
Must have
• Organisational Logo as prominent logo
"Funded by" logos (Marrowind Authority and Kerbwise)

```html
<!DOCTYPE html>
<html lang="en">
<head>
<meta charset="utf-8">
<title>Sunrise Table Breakfast – HVYN</title>
<link rel="stylesheet" href="https://fonts.googleapis.com/css2?family=Arimo:wght@400;700&family=Gochi+Hand&display=swap">
<style>
  :root {
    --paper: #ffffff;
    --orange: #f15a3b;
    --brown: #6a3f1c;
    --address: #5a4322;
    --blue: #1f5fb0;
    --ink: #222222;
    --badge: #c9d62a;
    --photo-warm: #e7c08a;
    --photo-cream: #f6eee4;
    --photo-dark: #6b4a36;
  }
  * { margin: 0; padding: 0; box-sizing: border-box; }
  html, body { width: 900px; height: 1200px; overflow: hidden; background: var(--paper); }
  .flyer {
    position: relative;
    width: 900px;
    height: 1200px;
    background: var(--paper);
    font-family: "Arimo", Arial, sans-serif;
    overflow: hidden;
  }
  .hero-photo {
    position: absolute;
    left: 0; top: 0;
    width: 900px; height: 555px;
    background:
      radial-gradient(ellipse 55% 40% at 52% 62%, var(--photo-warm) 0%, rgba(231,192,138,0.6) 45%, transparent 75%),
      radial-gradient(ellipse 35% 30% at 55% 40%, var(--photo-cream) 0%, transparent 70%),
      linear-gradient(180deg, var(--photo-dark) 0%, #b89a86 22%, #eee6e0 45%, #f3ece6 100%);
  }
  .headline {
    position: absolute;
    left: 33px; top: 462px;
    font-size: 103px;
    font-weight: 700;
    color: var(--paper);
    letter-spacing: -2px;
    line-height: 1;
    white-space: nowrap;
  }
  .headline-question {
    position: absolute;
    left: 103px; top: 545px;
    font-size: 74px;
    font-weight: 700;
    color: var(--orange);
    letter-spacing: -1px;
    line-height: 1;
  }
  .org-mark {
    position: absolute;
    left: 108px; top: 650px;
    display: flex;
    align-items: center;
    gap: 16px;
  }
  .org-mark .dot {
    width: 62px; height: 62px;
    border-radius: 50%;
    background: var(--blue);
  }
  .org-mark .org-name {
    font-size: 78px;
    font-weight: 700;
    color: var(--blue);
    letter-spacing: -2px;
    line-height: 1;
  }
  .org-full-name {
    position: absolute;
    left: 108px; top: 738px;
    font-size: 14px;
    font-weight: 700;
    color: var(--blue);
    letter-spacing: 0.5px;
  }
  .frequency {
    position: absolute;
    left: 90px; top: 808px;
    font-family: "Gochi Hand", cursive;
    font-size: 50px;
    color: var(--brown);
    transform: rotate(-8deg);
    transform-origin: left bottom;
    line-height: 1;
  }
  .hours {
    position: absolute;
    left: 92px; top: 864px;
    font-size: 34px;
    font-weight: 700;
    color: var(--orange);
    line-height: 1;
  }
  .audience {
    position: absolute;
    left: 90px; top: 926px;
    font-size: 38px;
    font-weight: 700;
    color: var(--orange);
    line-height: 36px;
    letter-spacing: -0.5px;
  }
  .contact {
    position: absolute;
    left: 92px; top: 1020px;
    font-size: 24px;
    font-weight: 700;
    color: var(--address);
    line-height: 24px;
    font-style: normal;
  }
  .funders {
    position: absolute;
    left: 700px; top: 892px;
    width: 146px;
    display: flex;
    flex-direction: column;
    align-items: center;
    color: var(--ink);
  }
  .funders .label { font-size: 10px; margin-bottom: 18px; }
  .funder-authority { display: flex; flex-direction: column; align-items: center; gap: 6px; }
  .funder-authority .dot {
    width: 42px; height: 42px; border-radius: 50%; background: var(--blue);
  }
  .funder-authority .name {
    font-size: 14px; font-weight: 700; text-align: center; line-height: 15px; color: var(--ink);
  }
  .funder-kerbwise { margin-top: 28px; display: flex; flex-direction: column; align-items: center; gap: 6px; }
  .funder-kerbwise .badge { width: 118px; height: 76px; background: var(--badge); }
  .funder-kerbwise .name { font-size: 14px; font-weight: 700; color: var(--ink); }
</style>
</head>
<body>
  <main class="flyer">
    <div class="hero-photo" role="img" aria-label="Photo of a pancake topped with whipped cream, a scoop of ice cream and sliced strawberries, with a small jug of syrup behind"></div>

    <h1 class="headline">Free Breakfast</h1>
    <p class="headline-question">anyone?</p>

    <div class="org-mark">
      <span class="dot"></span>
      <span class="org-name">HVYN</span>
    </div>
    <p class="org-full-name">Harlow Valley Youth Network</p>

    <p class="frequency">Every week!</p>
    <p class="hours">8am-9:30pm</p>
    <p class="audience">All young people<br>25 and under!</p>

    <address class="contact">HVYN<br>42 Fenwick Rd.<br>Harlow<br>Ph: 3907 4426</address>

    <aside class="funders">
      <span class="label">Funded by</span>
      <div class="funder-authority">
        <span class="dot"></span>
        <span class="name">Marrowind<br>Authority</span>
      </div>
      <div class="funder-kerbwise">
        <span class="badge"></span>
        <span class="name">Kerbwise</span>
      </div>
    </aside>
  </main>
</body>
</html>
```